New website for our Escape Room

We are wanting to create a new website for our website. We have 2 different locations that guests will choose their location on the home page. Then we have 5 different escape room experiences. We like clean and fresh but fun. Our logo is black white and red. We like a modern feel that is simple to navigate. I love movement on the page. You can see our current site at quillhornpuzzles.com
We like fresh and modern. It needs to include much of the same information as out current site but we won't like the look of our site.

Target Market(s)

amusement, escape rooms.

Industry/Entity Type

escape room

Number of Pages Required

4 page

Requirements
Must have
• info on all 4 escape rooms, option to choose between Pigeon Forge and Nashville locations.

```html
<!DOCTYPE html>
<html lang="en">
<head>
<meta charset="utf-8">
<title>Quillhorn Escape Game</title>
<link href="https://fonts.googleapis.com/css2?family=Bebas+Neue&family=Roboto:wght@400;500;700&family=Roboto+Condensed:wght@400;700&display=swap" rel="stylesheet">
<style>
:root{
  --red:#ff0000;
  --red-deep:#c40000;
  --black:#000;
  --panel:#0c0c0c;
  --card:#161616;
  --white:#fff;
  --grey:#cfcfcf;
}
*{margin:0;padding:0;box-sizing:border-box}
html,body{width:1200px;height:4542px;overflow:hidden;background:var(--black);color:var(--white);font-family:'Roboto',Arial,sans-serif}
.page{position:relative;width:1200px;height:4542px}
.block{position:absolute;left:0;width:1200px}
.display{font-family:'Bebas Neue',Impact,sans-serif;font-weight:400;letter-spacing:.5px}
.bracket{
  border-left:2px solid var(--red);border-right:2px solid var(--red);
  background:
    linear-gradient(var(--red),var(--red)) left top/12px 2px no-repeat,
    linear-gradient(var(--red),var(--red)) right top/12px 2px no-repeat,
    linear-gradient(var(--red),var(--red)) left bottom/12px 2px no-repeat,
    linear-gradient(var(--red),var(--red)) right bottom/12px 2px no-repeat;
}
.btn{position:absolute;display:flex;align-items:center;justify-content:center;font-family:'Roboto Condensed',Arial,sans-serif;font-weight:700;font-size:11px;text-transform:uppercase;color:var(--white)}
.section-title{position:absolute;left:50%;transform:translateX(-50%);padding:6px 14px 2px;font-family:'Bebas Neue',Impact,sans-serif;font-size:33px;white-space:nowrap}
.frame-svg{position:absolute;left:0;top:0}

/* header */
.header{top:0;height:97px}
.brand{position:absolute;left:132px;top:6px;font-family:'Bebas Neue',Impact,sans-serif;font-size:40px;letter-spacing:1px}
.phone{position:absolute;top:12px;height:32px;display:flex;align-items:center;gap:7px;padding:0 12px;font-size:11px;font-weight:500}
.social{position:absolute;top:14px;width:28px;height:28px;border:2px solid var(--red)}
.nav{position:absolute;top:103px;left:0;width:1200px;height:18px;z-index:3}
.nav span{position:absolute;font-size:10.5px;font-weight:500;text-transform:uppercase}

/* hero */
.hero{top:53px;height:572px}
.hero-photo{position:absolute;left:32px;top:44px;width:1134px;height:493px;background:radial-gradient(ellipse at 50% 40%,#5a1416 0%,#2a0a0b 45%,#0b0505 100%)}
.hero-title{position:absolute;top:188px;width:1200px;text-align:center;font-size:66px}
.hero-text{position:absolute;top:276px;left:190px;width:820px;text-align:center;font-size:12px;line-height:23px}
.dots{position:absolute;top:490px;left:582px;display:flex;gap:4px}
.dots i{width:7px;height:7px;border-radius:50%;background:var(--white)}
.dots i:first-child{background:var(--red)}

/* about */
.about{top:625px;height:415px}
.about p{position:absolute;left:190px;width:820px;text-align:center;font-size:12px;line-height:22px;color:var(--white)}
.about em{font-style:normal;color:var(--red)}

/* rooms */
.rooms{top:1040px;height:669px}
.room{position:absolute;overflow:hidden}
.room .photo{position:absolute;inset:0}
.room .name{position:absolute;left:0;width:100%;text-align:center;font-family:'Bebas Neue',Impact,sans-serif;font-size:22px}
.room-feature{background:var(--red-deep)}
.room-feature p{position:absolute;left:22px;width:233px;top:150px;text-align:center;font-size:10.5px;line-height:20px}

/* benefits */
.benefits{top:1709px;height:485px}
.benefit{position:absolute;top:187px;width:176px;height:210px;background:var(--card);border-radius:10px;text-align:center}
.benefit .ico{position:absolute;left:50%;top:16px;width:74px;height:66px;transform:translateX(-50%);display:flex;align-items:center;justify-content:center}
.benefit .kicker{position:absolute;top:104px;width:100%;font-size:9.5px;color:var(--red);text-transform:uppercase}
.benefit .label{position:absolute;top:120px;width:100%;font-family:'Roboto Condensed',Arial,sans-serif;font-weight:700;font-size:12px;line-height:23px;text-transform:uppercase}
.benefit .go{position:absolute;left:50%;bottom:14px;width:38px;height:20px;transform:translateX(-50%);display:flex;align-items:center;justify-content:center}

/* locations */
.locations{top:2194px;height:511px;background:var(--panel)}
.location{position:absolute;top:167px;width:389px;height:256px}
.location .inner{position:absolute;left:21px;top:28px;width:347px;height:201px;background:var(--black);text-align:center}
.location .name{font-family:'Bebas Neue',Impact,sans-serif;font-size:40px;line-height:1;padding-top:18px;color:var(--white)}
.location .place{font-family:'Roboto Condensed',Arial,sans-serif;font-weight:700;font-size:13px;text-transform:uppercase;margin-top:8px;color:var(--white)}
.location .info{font-size:11.5px;line-height:21px;margin:8px auto 0;width:300px;text-transform:uppercase}

/* audience */
.audience{top:2705px;height:669px}
.aud-photo{position:absolute;left:670px;top:30px;width:496px;height:595px;background:linear-gradient(160deg,#5c5c5c 0%,#2b2b2b 55%,#111 100%)}
.aud-title{position:absolute;left:132px;top:168px;width:48px;height:342px;display:flex;align-items:center;justify-content:center}
.aud-title span{transform:rotate(-90deg);white-space:nowrap;font-family:'Bebas Neue',Impact,sans-serif;font-size:33px}
.aud-item{position:absolute;left:233px;width:420px}
.aud-item .badge{position:absolute;left:0;top:0;width:58px;height:58px;background:var(--red);display:flex;align-items:center;justify-content:center}
.aud-item h3{position:absolute;left:75px;top:-14px;font-family:'Bebas Neue',Impact,sans-serif;font-weight:400;color:var(--red);font-size:20px;white-space:nowrap}
.aud-item p{position:absolute;left:75px;top:12px;width:345px;font-size:10.5px;line-height:22px}

/* escapists */
.escapists{top:3374px;height:740px}
.shot{position:absolute;width:262px;height:242px;background:linear-gradient(180deg,#2e2e2e 0%,#1c1c1c 60%,#3a1010 100%)}

/* footer */
.footer{top:4114px;height:428px}
.footer-inner{position:absolute;left:32px;top:41px;width:1134px;height:387px;background:var(--panel)}
.footer-brand{position:absolute;top:105px;width:1200px;text-align:center;font-family:'Bebas Neue',Impact,sans-serif;font-size:84px;letter-spacing:2px}
.footer-nav span{position:absolute;top:232px;font-size:10.5px;font-weight:500;text-transform:uppercase}
.footer-rule{position:absolute;left:132px;top:270px;width:936px;height:1px;background:#333}
.contact{position:absolute;top:290px;display:flex;align-items:center;gap:12px;font-size:12px}
.contact .dot{width:32px;height:32px;border-radius:50%;background:var(--red);display:flex;align-items:center;justify-content:center}
.copy{position:absolute;top:370px;width:1200px;text-align:center;font-size:10px;color:var(--grey)}
.copy b{color:var(--red);font-weight:400}
</style>
</head>
<body>
<div class="page">

  <section class="block hero">
    <svg class="frame-svg" width="1200" height="572" viewBox="0 0 1200 572">
      <polygon points="0,0 290,44 910,44 1200,0 1200,572 910,537 290,537 0,572" fill="#ff0000"/>
    </svg>
    <div class="hero-photo" role="img" aria-label="Dark red maze of walls stretching into the distance"></div>
    <h1 class="display hero-title">Welcome to Quillhorn</h1>
    <p class="hero-text">QUILLHORN ESCAPE GAME is the heart pounding, code-cracking, mind-bending race against time experience that will require everyone in your group's collective intellect, ingenuity, and problem-solving skills to escape.</p>
    <div class="btn bracket" style="left:455px;top:338px;width:128px;height:36px">Pigeon Forge</div>
    <div class="btn bracket" style="left:617px;top:338px;width:128px;height:36px">Nashville</div>
    <div class="dots"><i></i><i></i><i></i><i></i></div>
  </section>

  <header class="block header">
    <div class="brand">QUILLHORN</div>
    <div class="phone bracket" style="left:449px">
      <svg width="12" height="12" viewBox="0 0 24 24"><path fill="#ff0000" d="M6.6 10.8c1.4 2.8 3.8 5.1 6.6 6.6l2.2-2.2c.3-.3.7-.4 1-.2 1.1.4 2.3.6 3.6.6.6 0 1 .4 1 1V20c0 .6-.4 1-1 1C10.6 21 3 13.4 3 4c0-.6.4-1 1-1h3.5c.6 0 1 .4 1 1 0 1.2.2 2.4.6 3.6.1.3 0 .7-.2 1z"/></svg>
      629-555-0148
    </div>
    <div class="phone bracket" style="left:625px">
      <svg width="12" height="12" viewBox="0 0 24 24"><path fill="#ff0000" d="M6.6 10.8c1.4 2.8 3.8 5.1 6.6 6.6l2.2-2.2c.3-.3.7-.4 1-.2 1.1.4 2.3.6 3.6.6.6 0 1 .4 1 1V20c0 .6-.4 1-1 1C10.6 21 3 13.4 3 4c0-.6.4-1 1-1h3.5c.6 0 1 .4 1 1 0 1.2.2 2.4.6 3.6.1.3 0 .7-.2 1z"/></svg>
      865-555-0172
    </div>
    <div class="social" style="left:951px" role="img" aria-label="Social link"></div>
    <div class="social" style="left:995px" role="img" aria-label="Social link"></div>
    <div class="social" style="left:1039px" role="img" aria-label="Social link"></div>
    <nav class="nav">
      <span style="left:263px">Home</span>
      <span style="left:347px">About us</span>
      <span style="left:453px">Escape rooms &#9662;</span>
      <span style="left:600px">FAQ</span>
      <span style="left:670px">Gallery</span>
      <span style="left:771px">Gift cards</span>
      <span style="left:886px">Contact</span>
    </nav>
  </header>

  <section class="block about">
    <h2 class="section-title bracket" style="top:53px">About Quillhorn Escape Game</h2>
    <p style="top:132px">Quillhorn Escape Game is the <em>heart-pounding, code-cracking, mind-bending race-against-time</em> experience that Nashville and Pigeon Forge have been waiting for. With five unique experiences to choose from, our escape rooms offer a sense of adventure that only children's activities can match. However, our escape rooms are not for the faint of heart.</p>
    <p style="top:220px">We offer clean fun in a safe environment, but because we have some of the best escape rooms with horror themes, they can be seen as scary. Once you step inside the room, you are trapped, and anyone leaving the room early will disqualify your team's times from the leaderboard.</p>
    <div class="btn bracket" style="left:535px;top:312px;width:130px;height:40px">Learn more</div>
  </section>

  <section class="block rooms">
    <svg class="frame-svg" width="1200" height="669" viewBox="0 0 1200 669">
      <polygon points="0,0 300,35 900,35 1200,0 1200,669 900,643 300,643 0,669" fill="#ff0000"/>
      <rect x="32" y="35" width="1134" height="608" fill="#0c0c0c"/>
    </svg>
    <h2 class="section-title bracket" style="top:102px">Find the right room for you</h2>

    <div class="room" style="left:176px;top:176px;width:274px;height:188px">
      <div class="photo" role="img" aria-label="Prison island room scene with lighthouse icon" style="background:linear-gradient(135deg,#3a3a3a,#141414)"></div>
      <div class="name" style="top:130px">Alcatraz</div>
    </div>
    <div class="room room-feature" style="left:462px;top:176px;width:276px;height:393px">
      <div class="photo" role="img" aria-label="Asylum room scene with restraint chair icon" style="background:linear-gradient(180deg,#b30000 0%,#d40000 100%)"></div>
      <div class="name" style="top:100px">Asylum</div>
      <p>Whether you've dreamed of working as a spy, experiencing life in an asylum, or bringing evil people to justice, you're sure to get the experience you want in the Asylum escape room at Quillhorn Escape Game in Tennessee. Marrowfield Psychiatric Asylum is not only one of the oldest asylums, but is reportedly one of the most abusive. Rumors say that there have.</p>
      <div class="btn bracket" style="left:72px;top:327px;width:130px;height:42px">Learn more</div>
    </div>
    <div class="room" style="left:749px;top:176px;width:275px;height:188px">
      <div class="photo" role="img" aria-label="Captured room scene with bound hands icon" style="background:linear-gradient(135deg,#1c1c1c,#3a3a3a 70%,#b00000 92%)"></div>
      <div class="name" style="top:130px">Captured</div>
    </div>
    <div class="room" style="left:176px;top:382px;width:274px;height:187px">
      <div class="photo" role="img" aria-label="Apocalypse room scene with gas mask icon" style="background:linear-gradient(135deg,#4a4a4a,#181818 70%,#8a0000 95%)"></div>
      <div class="name" style="top:130px">Apocalypse</div>
    </div>
    <div class="room" style="left:749px;top:382px;width:275px;height:187px">
      <div class="photo" role="img" aria-label="Haunted cabin room scene with cabin icon" style="background:linear-gradient(135deg,#2a2222,#3c3434)"></div>
      <div class="name" style="top:130px">Haunted Cabin</div>
    </div>
  </section>

  <section class="block benefits">
    <h2 class="section-title bracket" style="top:58px">Discover the benefits of escape rooms</h2>
    <p style="position:absolute;top:127px;width:1200px;text-align:center;font-size:12px">Escape rooms are fun foster teamwork and give you a sense of accomplishment</p>

    <div class="benefit" style="left:128px">
      <div class="ico bracket"><svg width="40" height="40" viewBox="0 0 40 40" fill="none" stroke="#fff" stroke-width="1.6"><circle cx="13" cy="14" r="5"/><circle cx="27" cy="14" r="5"/><path d="M4 34c0-6 4-10 9-10s9 4 9 10M18 34c0-6 4-10 9-10s9 4 9 10"/></svg></div>
      <div class="kicker">Improve</div>
      <div class="label">Communication and<br>social skills</div>
      <div class="go bracket"><svg width="20" height="10" viewBox="0 0 20 10"><path d="M1 5h17M13 1l5 4-5 4" stroke="#fff" stroke-width="1.4" fill="none"/></svg></div>
    </div>
    <div class="benefit" style="left:320px">
      <div class="ico bracket"><svg width="40" height="40" viewBox="0 0 40 40" fill="none" stroke="#fff" stroke-width="1.6"><path d="M12 36v-8c-4-3-6-7-5-12 2-7 9-10 15-8 6 2 9 8 7 14l3 5-4 1v6h-7"/><circle cx="19" cy="17" r="4"/></svg></div>
      <div class="kicker">Challenge your</div>
      <div class="label">Creative thinking and<br>problem solving skills</div>
      <div class="go bracket"><svg width="20" height="10" viewBox="0 0 20 10"><path d="M1 5h17M13 1l5 4-5 4" stroke="#fff" stroke-width="1.4" fill="none"/></svg></div>
    </div>
    <div class="benefit" style="left:512px">
      <div class="ico bracket"><svg width="40" height="40" viewBox="0 0 40 40" fill="none" stroke="#fff" stroke-width="1.6"><ellipse cx="20" cy="20" rx="14" ry="12"/><path d="M20 8v24M13 14c3 0 4 3 7 3M27 24c-3 0-4-3-7-3M10 22h5M25 16h5"/></svg></div>
      <div class="kicker">Enhance and</div>
      <div class="label">Build<br>your memory</div>
      <div class="go bracket"><svg width="20" height="10" viewBox="0 0 20 10"><path d="M1 5h17M13 1l5 4-5 4" stroke="#fff" stroke-width="1.4" fill="none"/></svg></div>
    </div>
    <div class="benefit" style="left:704px">
      <div class="ico bracket"><svg width="40" height="40" viewBox="0 0 40 40" fill="none" stroke="#fff" stroke-width="1.6"><circle cx="20" cy="20" r="14"/><circle cx="15" cy="17" r="1.5" fill="#fff"/><circle cx="25" cy="17" r="1.5" fill="#fff"/><path d="M13 24c3 4 11 4 14 0"/></svg></div>
      <div class="kicker">Improve</div>
      <div class="label">Your mood</div>
      <div class="go bracket"><svg width="20" height="10" viewBox="0 0 20 10"><path d="M1 5h17M13 1l5 4-5 4" stroke="#fff" stroke-width="1.4" fill="none"/></svg></div>
    </div>
    <div class="benefit" style="left:896px">
      <div class="ico bracket"><svg width="40" height="40" viewBox="0 0 40 40" fill="none" stroke="#fff" stroke-width="1.6"><path d="M14 22a7 7 0 1 1 12 0c-2 2-2 4-2 6h-8c0-2 0-4-2-6zM16 32h8M17 35h6M20 4v3M8 10l2 2M32 10l-2 2M5 20h3M35 20h-3"/></svg></div>
      <div class="kicker">Increase your</div>
      <div class="label">Attention to detail</div>
      <div class="go bracket"><svg width="20" height="10" viewBox="0 0 20 10"><path d="M1 5h17M13 1l5 4-5 4" stroke="#fff" stroke-width="1.4" fill="none"/></svg></div>
    </div>
  </section>

  <section class="block locations">
    <h2 class="section-title bracket" style="top:89px">Find our locations</h2>
    <div class="location" style="left:192px">
      <svg class="frame-svg" width="389" height="256" viewBox="0 0 389 256"><polygon points="0,0 389,12 378,256 0,244" fill="#ff0000"/></svg>
      <div class="inner">
        <div class="name">QUILLHORN</div>
        <div class="place">Nashville</div>
        <div class="info">Wheelchair accessible rooms<br>at Nashville: Asylum</div>
        <div class="btn bracket" style="left:108px;top:152px;width:130px;height:38px">Book now</div>
      </div>
    </div>
    <div class="location" style="left:620px">
      <svg class="frame-svg" width="389" height="256" viewBox="0 0 389 256"><polygon points="0,12 389,0 389,244 11,256" fill="#ff0000"/></svg>
      <div class="inner">
        <div class="name">QUILLHORN</div>
        <div class="place">Pigeon Forge</div>
        <div class="info">Wheelchair accessible rooms at Pigeon Forge: Kingpin, Haunted Cabin, Asylum</div>
        <div class="btn bracket" style="left:108px;top:152px;width:130px;height:38px">Book now</div>
      </div>
    </div>
  </section>

  <section class="block audience">
    <svg class="frame-svg" width="1200" height="669" viewBox="0 0 1200 669">
      <polygon points="0,0 300,30 900,30 1200,0 1200,669 900,625 300,625 0,669" fill="#ff0000"/>
      <rect x="32" y="30" width="1134" height="595" fill="#000"/>
      <line x1="262" y1="140" x2="262" y2="520" stroke="#ff0000" stroke-width="1.5" stroke-dasharray="4 4"/>
      <line x1="180" y1="340" x2="262" y2="340" stroke="#ff0000" stroke-width="1.5"/>
    </svg>
    <div class="aud-photo" role="img" aria-label="Player with backpack climbing wooden steps outside a weathered barn"></div>
    <div class="aud-title bracket"><span>Who enjoys our rooms</span></div>

    <div class="aud-item" style="top:111px">
      <div class="badge"><svg width="30" height="30" viewBox="0 0 30 30" fill="none" stroke="#fff" stroke-width="1.8"><path d="M6 8l8 8M14 8l-8 8M16 14l8 8M24 14l-8 8M10 24l10-18"/></svg></div>
      <h3>Team building</h3>
      <p>What better way to foster synergy and teamwork than to be locked in a room together? Quillhorn escape games offer a one-of-a-kind team-building experience for corporate organizations.</p>
    </div>
    <div class="aud-item" style="top:238px">
      <div class="badge"><svg width="32" height="22" viewBox="0 0 32 22" fill="none" stroke="#fff" stroke-width="1.8"><path d="M8 2h16a7 7 0 0 1 7 8l-1 7a4 4 0 0 1-7 1l-2-3h-10l-2 3a4 4 0 0 1-7-1l-1-7a7 7 0 0 1 7-8z"/><path d="M9 8v5M6.5 10.5h5"/><circle cx="22" cy="9" r="1" fill="#fff"/><circle cx="25" cy="12" r="1" fill="#fff"/></svg></div>
      <h3>Gamers</h3>
      <p>Have you been looking for a way to impress your friends with your amazing cryptogram skills? Looking to take your strategic skills to an adventurous activity outside of the screen.</p>
    </div>
    <div class="aud-item" style="top:365px">
      <div class="badge"><svg width="32" height="30" viewBox="0 0 32 30" fill="none" stroke="#fff" stroke-width="1.8"><circle cx="9" cy="12" r="3"/><circle cx="23" cy="12" r="3"/><circle cx="16" cy="18" r="2.2"/><path d="M4 29v-8h10v8M18 29v-8h10v8M13 29v-5h6v5M14 4c0-2 4-2 2 1l-2 2-2-2c-2-3 2-3 2-1z"/></svg></div>
      <h3>Friends and family</h3>
      <p>Bring your family, friends, neighbors, or a stranger you just met, and join us for an action-packed 60 minutes that you won't forget! When you need fun family activities or you and your friends are looking.</p>
    </div>
    <div class="aud-item" style="top:492px">
      <div class="badge"><svg width="24" height="30" viewBox="0 0 24 30" fill="none" stroke="#fff" stroke-width="1.8"><path d="M12 28s-10-10-10-17a10 10 0 0 1 20 0c0 7-10 17-10 17z"/><circle cx="12" cy="11" r="4"/></svg></div>
      <h3>Tourists and visitors</h3>
      <p>Looking for an interactive experience for your entire group to enjoy together? Located only a short distance from downtown Pigeon Forge and Nashville, Quillhorn Escape Game offers.</p>
    </div>
  </section>

  <section class="block escapists">
    <h2 class="section-title bracket" style="top:57px">Our succesfull escapists</h2>
    <svg class="frame-svg" width="1200" height="740" viewBox="0 0 1200 740">
      <polygon points="106,110 948,125 948,140 128,140 128,366 250,366 250,382 106,390" fill="#ff0000"/>
      <polygon points="1078,382 1078,680 228,680 228,666 1060,666 1060,396 950,396 950,380" fill="#ff0000"/>
    </svg>
    <div class="shot" style="left:128px;top:143px" role="img" aria-label="Group of players posing after escaping"></div>
    <div class="shot" style="left:403px;top:143px" role="img" aria-label="Team holding winner signs after escaping"></div>
    <div class="shot" style="left:678px;top:143px" role="img" aria-label="Friends holding a photo frame prop after escaping"></div>
    <div class="shot" style="left:248px;top:398px" role="img" aria-label="Family group posing after completing a room"></div>
    <div class="shot" style="left:523px;top:398px" role="img" aria-label="Couple holding escape signs"></div>
    <div class="shot" style="left:797px;top:398px" role="img" aria-label="Large group celebrating a successful escape"></div>
  </section>

  <footer class="block footer">
    <svg class="frame-svg" width="1200" height="428" viewBox="0 0 1200 428">
      <polygon points="0,0 300,41 900,41 1200,0 1200,428 0,428" fill="#ff0000"/>
    </svg>
    <div class="footer-inner"></div>
    <div class="footer-brand">QUILLHORN</div>
    <div class="footer-nav">
      <span style="left:266px">Home</span>
      <span style="left:351px">About us</span>
      <span style="left:458px">Escape rooms</span>
      <span style="left:595px">FAQ</span>
      <span style="left:665px">Gallery</span>
      <span style="left:765px">Gift cards</span>
      <span style="left:881px">Contact</span>
    </div>
    <div class="footer-rule"></div>
    <div class="contact" style="left:158px">
      <div class="dot"><svg width="14" height="18" viewBox="0 0 24 30" fill="none" stroke="#fff" stroke-width="2.4"><path d="M12 28s-10-10-10-17a10 10 0 0 1 20 0c0 7-10 17-10 17z"/><circle cx="12" cy="11" r="4"/></svg></div>
      1180 Larkspur Lane, Nashville, TN 37204
    </div>
    <div class="contact" style="left:541px">
      <div class="dot"><svg width="14" height="14" viewBox="0 0 24 24"><path fill="#fff" d="M6.6 10.8c1.4 2.8 3.8 5.1 6.6 6.6l2.2-2.2c.3-.3.7-.4 1-.2 1.1.4 2.3.6 3.6.6.6 0 1 .4 1 1V20c0 .6-.4 1-1 1C10.6 21 3 13.4 3 4c0-.6.4-1 1-1h3.5c.6 0 1 .4 1 1 0 1.2.2 2.4.6 3.6.1.3 0 .7-.2 1z"/></svg></div>
      629-555-0148
    </div>
    <div class="contact" style="left:778px">
      <div class="dot"><svg width="16" height="12" viewBox="0 0 16 12" fill="none" stroke="#fff" stroke-width="1.4"><rect x="1" y="1" width="14" height="10"/><path d="M1 1l7 6 7-6"/></svg></div>
      nashville@quillhornpuzzles.com
    </div>
    <div class="copy">2022 copyrights &copy; <b>Quillhorn Escape Game</b> &nbsp;| &nbsp;&nbsp;All rights reserved.</div>
  </footer>

</div>
</body>
</html>
```